Design a label for Copper Harbor e liquid company

need a logo and five different fonts for each flavor
1. hooray hooray wow_ confetti cream cake
2. Red Velvet- red velvet Cake
3, Tiramisu- lady fingers soaked in expresso
4. Crumb Castle- apple cinnamon muffin
5. Glen Fold- blueberry turn over
these labels are going to be two different bottle sizes
30 ml and 60 ml with 3 different nicotine strengths
Target Market(s)
vapors that want dessert flavors
Industry/Entity Type
It Company
Contact Information for Business Card
will supply logo
Other font styles liked:
- custom
Colors
Designer to choose colors to be used in the design.
Requirements
Must have
- custom logo and fonts
Nice to have
- ai files for multi color foil label printing

```html
<!DOCTYPE html>
<html lang="en">
<head>
<meta charset="utf-8">
<title>Copper Harbor – Red Velvet Label</title>
<link rel="stylesheet" href="https://fonts.googleapis.com/css2?family=Lobster&family=Roboto:wght@700&display=swap">
<style>
  :root {
    --stage-bg: #d9d9d9;
    --label-pink-light: #e2306f;
    --label-pink-deep: #c5124f;
    --label-cream: #f3f3f3;
    --ink-dark: #1c1c1c;
    --ink-white: #ffffff;
  }
  html, body {
    margin: 0;
    padding: 0;
    width: 1200px;
    height: 840px;
    overflow: hidden;
    background: var(--stage-bg);
  }
  .stage {
    position: relative;
    width: 1200px;
    height: 840px;
  }
  .label {
    position: absolute;
    left: 333px;
    top: 0;
    width: 534px;
    height: 840px;
    background: linear-gradient(160deg, var(--label-pink-light) 0%, var(--label-pink-deep) 100%);
    overflow: hidden;
  }
  .brand-arch {
    position: absolute;
    left: 92px;
    top: 0;
    width: 350px;
    height: 378px;
    background: var(--label-cream);
    border-radius: 0 0 175px 175px;
  }
  .brand-mark {
    position: absolute;
    left: 0;
    right: 0;
    top: 96px;
    display: flex;
    flex-direction: column;
    align-items: center;
    gap: 14px;
  }
  .brand-dot {
    width: 46px;
    height: 46px;
  }
  .brand-name {
    font-family: "Lobster", cursive;
    font-size: 46px;
    line-height: 1;
    color: var(--ink-dark);
    margin: 0;
  }
  .flavor-name {
    position: absolute;
    left: 0;
    right: 0;
    top: 472px;
    margin: 0;
    text-align: center;
    font-family: "Lobster", cursive;
    font-weight: 400;
    font-size: 84px;
    line-height: 1;
    color: var(--ink-white);
    text-shadow: 0 2px 3px rgba(0,0,0,0.25);
  }
  .flavor-note {
    position: absolute;
    left: 0;
    right: 0;
    top: 578px;
    margin: 0;
    text-align: center;
    font-family: "Lobster", cursive;
    font-size: 44px;
    line-height: 1;
    color: var(--ink-white);
    text-shadow: 0 2px 3px rgba(0,0,0,0.25);
  }
  .volume {
    position: absolute;
    left: 0;
    right: 0;
    top: 798px;
    margin: 0;
    text-align: center;
    font-family: "Roboto", sans-serif;
    font-weight: 700;
    font-size: 24px;
    color: var(--ink-white);
  }
</style>
</head>
<body>
  <main class="stage">
    <section class="label">
      <div class="brand-arch">
        <div class="brand-mark">
          <svg class="brand-dot" viewBox="0 0 46 46" aria-hidden="true">
            <circle cx="23" cy="23" r="21" fill="none" stroke="#1c1c1c" stroke-width="4"/>
          </svg>
          <p class="brand-name">Copper Harbor</p>
        </div>
      </div>
      <h1 class="flavor-name">Red Velvet</h1>
      <p class="flavor-note">Red Velvet Cake</p>
      <p class="volume">30ml</p>
    </section>
  </main>
</body>
</html>
```